Brisco Interiors

Hi, can you please make this design up for me. Brisco interiors text to front and Philippa Brisco text to back in black. Small love hearts to be black. Mobile number to front text and back mobile number and email address text to be white. Open to your input 🙂 Thanks in advance! Philippa

Industry/Entity Type

Interior Design

Colors

Designer to choose only greyscale colors for use in the design.

Requirements
Must have
• Little love hearts for dot on i

```html
<!DOCTYPE html>
<html lang="en">
<head>
<meta charset="utf-8">
<title>Brisco Interiors – Business Card</title>
<link rel="stylesheet" href="https://fonts.googleapis.com/css2?family=Didact+Gothic&display=swap">
<style>
  :root {
    --backdrop: #dcdcdc;
    --card-light: #f7f6f1;
    --card-dark: #0b0b0b;
    --ink-dark: #111111;
    --ink-light: #efeee8;
    --shadow: rgba(0, 0, 0, 0.22);
  }
  * { box-sizing: border-box; margin: 0; padding: 0; }
  html, body {
    width: 1200px;
    height: 787px;
    overflow: hidden;
    background: var(--backdrop);
    font-family: "Didact Gothic", "Century Gothic", sans-serif;
  }
  .canvas {
    width: 1200px;
    height: 787px;
    display: flex;
    align-items: center;
    justify-content: center;
    gap: 60px;
  }
  .card {
    position: relative;
    width: 525px;
    height: 315px;
    box-shadow: 0 6px 18px var(--shadow);
  }
  .card--front { background: var(--card-light); color: var(--ink-dark); }
  .card--back  { background: var(--card-dark);  color: var(--ink-light); }

  .details {
    position: absolute;
    left: 38px;
    top: 176px;
  }
  .details__name {
    font-size: 31px;
    letter-spacing: 0.3px;
    line-height: 1.1;
    white-space: nowrap;
  }
  .card--back .details__name { font-size: 27px; letter-spacing: 0.8px; }
  .details__row {
    display: flex;
    align-items: center;
    gap: 7px;
    font-size: 17px;
    letter-spacing: 0.6px;
    margin-top: 6px;
    white-space: nowrap;
  }
  .details__row--email { margin-left: 160px; margin-top: 10px; }
  .icon { width: 13px; height: 13px; fill: currentColor; flex: none; }

  .corner-dot {
    position: absolute;
    right: 44px;
    bottom: 46px;
    width: 22px;
    height: 22px;
    border-radius: 50%;
  }
  .card--front .corner-dot { background: var(--ink-dark); }
  .card--back .corner-dot  { background: var(--ink-light); }
</style>
</head>
<body>
<main class="canvas">
  <section class="card card--front" aria-label="Card front">
    <div class="details">
      <p class="details__name">Brisco interiors</p>
      <p class="details__row">
        <svg class="icon" viewBox="0 0 16 16" aria-hidden="true"><path d="M3.6 1.2l2.3 2.6-1.4 2c.9 2 2.6 3.8 4.7 4.8l2-1.4 2.6 2.3-1.2 2.3c-6.1-.6-10.7-5.2-11.3-11.3z"/></svg>
        000-000-000-000
      </p>
    </div>
    <span class="corner-dot" aria-hidden="true"></span>
  </section>

  <section class="card card--back" aria-label="Card back">
    <div class="details">
      <p class="details__name">Philippa Brisco</p>
      <p class="details__row">
        <svg class="icon" viewBox="0 0 16 16" aria-hidden="true"><path d="M3.6 1.2l2.3 2.6-1.4 2c.9 2 2.6 3.8 4.7 4.8l2-1.4 2.6 2.3-1.2 2.3c-6.1-.6-10.7-5.2-11.3-11.3z"/></svg>
        000-000-000-000
      </p>
      <p class="details__row details__row--email">
        <svg class="icon" viewBox="0 0 16 12" aria-hidden="true"><path d="M0 0h16v12H0z M1.5 1.5v.4L8 6.6l6.5-4.7v-.4z" fill-rule="evenodd"/></svg>
        hello@briscostudio.com
      </p>
    </div>
    <span class="corner-dot" aria-hidden="true"></span>
  </section>
</main>
</body>
</html>
```